Brindlow Electrical Solutions needs a website

We need a new website designed because our current one is outdated. I would like a one-page website. We are a B2B company and want to maintain a professional appearance to appeal to project managers and directors.

for some reference, these are a few of my competitor's websites; we offer the same services.

https://valtorwiring.com.au/services
https://www.dunsary.com.au/mechanical-electrical-services/
https://www.gravik.com.au/

Industry/Entity Type

Electrical

Number of Pages Required

1 page

Font styles to use
Sans Serif

Colors
0054AA
0677BA
7BADD7
CADEEF
E8F1F8

```html
<!DOCTYPE html>
<html lang="en">
<head>
<meta charset="utf-8">
<title>Brindlow Electrical Solutions</title>
<link href="https://fonts.googleapis.com/css2?family=Audiowide&family=Oswald:wght@500&family=Poppins:wght@400;500;600;700&display=swap" rel="stylesheet">
<style>
:root{
  --brand:#0b98e0;
  --brand-deep:#0054AA;
  --ink:#1b1b1b;
  --muted:#555;
  --line:#d9d9d9;
  --panel:#f4f4f4;
  --footer:#20292f;
  --white:#fff;
  --sky-a:#cadeef;
  --sky-b:#7badd7;
}
*{box-sizing:border-box;margin:0;padding:0}
html,body{width:1200px;height:4078px;overflow:hidden}
body{font-family:"Poppins",sans-serif;color:var(--ink);background:var(--white);position:relative}
.display{font-family:"Audiowide",sans-serif;text-transform:uppercase;font-weight:400}
.eyebrow{font-family:"Oswald",sans-serif;letter-spacing:5px;font-size:16px;text-transform:uppercase;color:var(--ink)}
.btn{display:inline-block;background:var(--brand);color:var(--white);font-weight:700;font-size:12px;text-transform:uppercase;border-radius:20px;padding:10px 14px;border:2px solid var(--white)}
.abs{position:absolute}

/* top bar */
.topbar{position:absolute;top:0;left:0;width:1200px;height:32px;background:var(--brand);color:var(--white);font-size:13px;display:flex;align-items:center;padding:0 62px;gap:26px}
.topbar span{display:flex;align-items:center;gap:6px}
.topbar .phone{margin-left:auto}
/* nav */
.nav{position:absolute;top:32px;left:0;width:1200px;height:66px;display:flex;align-items:center;padding:0 62px}
.logo{display:flex;align-items:center;gap:8px;font-weight:600;font-size:20px;color:var(--brand-deep)}
.logo i{width:38px;height:38px;border-radius:50%;background:var(--brand-deep);display:block}
.nav ul{list-style:none;display:flex;gap:42px;margin-left:auto;font-size:15px;margin-right:32px}
.nav li.active{font-weight:700}
.nav .btn{border:none;padding:11px 16px;font-size:13px}
/* hero */
.hero{position:absolute;top:98px;left:0;width:1200px;height:576px;background:linear-gradient(100deg,#1a1d2b 0%,#2b3350 45%,#3a4a78 70%,#6b6f8a 100%)}
.hero h1{position:absolute;left:66px;top:155px;font-size:40px;line-height:52px;color:var(--white)}
.hero p{position:absolute;left:66px;top:275px;width:570px;font-size:14.5px;line-height:22.5px;color:var(--white)}
.hero .btn{position:absolute;left:66px;top:386px;border:none;padding:10px 14px}
.dots{position:absolute;left:570px;top:538px;display:flex;gap:6px}
.dots b{width:9px;height:9px;border-radius:50%;background:var(--white)}
.dots b:first-child{background:var(--brand)}
/* about */
.about{position:absolute;top:674px;left:0;width:1200px;height:562px;background:var(--brand);color:var(--white)}
.about .photo{position:absolute;left:0;top:61px;width:606px;height:441px;border-radius:0 12px 12px 0;background:linear-gradient(135deg,#d8d2c8,#a69c8e 55%,#5f6468)}
.about .eyebrow{position:absolute;left:643px;top:60px;color:var(--white);font-size:15px}
.about h2{position:absolute;left:643px;top:96px;font-size:36px;line-height:43px}
.about p{position:absolute;left:643px;top:252px;width:360px;font-size:15px;line-height:22.5px}
.about ul{position:absolute;left:643px;top:350px;list-style:none;font-size:15px}
.about li{display:flex;align-items:center;gap:10px;height:34px}
.about .btn{position:absolute;left:643px;top:475px;background:var(--white);color:var(--brand);border:none}
/* services */
.services .eyebrow{position:absolute;top:1292px;width:1200px;text-align:center}
.sec-title{position:absolute;width:1200px;text-align:center;color:var(--brand);font-size:36px;line-height:44px}
.svc{position:absolute;top:1464px;width:343px;height:350px;border-radius:8px;overflow:hidden;border:1px solid var(--line);background:var(--white);box-shadow:0 3px 8px rgba(0,0,0,.08)}
.svc .head{height:153px;padding:18px 22px 0;text-align:center}
.svc h3{font-size:19px;line-height:23px;font-weight:700;text-transform:uppercase}
.svc p{font-size:14.5px;line-height:22px;margin-top:10px;color:var(--muted)}
.svc.dark .head{background:#6a6a6a;color:var(--white)}
.svc.dark h3{font-family:"Audiowide",sans-serif;font-weight:400}
.svc.dark p{color:var(--white)}
.svc .img{height:197px}
.center-btn{position:absolute;left:0;width:1200px;text-align:center}
.center-btn .btn{border:none;padding:11px 14px}
/* testimonials */
.quote-card{position:absolute;top:2153px;width:500px;height:282px;background:var(--panel);border:2px solid var(--line);border-radius:6px}
.avatar{position:absolute;left:40px;top:38px;width:74px;height:74px;border-radius:50%;background:linear-gradient(135deg,#8a7a6a,#c9b9a8)}
.quote-card h4{position:absolute;left:135px;top:52px;font-family:"Audiowide",sans-serif;font-weight:400;font-size:17px}
.quote-card .role{position:absolute;left:135px;top:80px;font-size:15px;color:var(--muted)}
.stars{position:absolute;right:40px;top:118px;color:#f28c1b;font-size:20px;letter-spacing:3px}
.quote-card blockquote{position:absolute;left:40px;top:154px;width:420px;font-size:14.5px;line-height:22.5px;font-weight:600}
.arrow{position:absolute;top:2466px;width:44px;height:44px;border-radius:50%;background:var(--brand);display:flex;align-items:center;justify-content:center}
/* projects */
.projects h2{position:absolute;left:63px;top:2570px;color:var(--brand);font-size:36px}
.proj{position:absolute;top:2648px;width:344px;height:374px;border-radius:18px;overflow:hidden}
.proj .tag{position:absolute;left:20px;bottom:22px;font-family:"Oswald",sans-serif;letter-spacing:5px;color:var(--white);font-size:17px;line-height:26px}
.proj .go{position:absolute;right:20px;bottom:28px;width:42px;height:42px;border-radius:50%;background:var(--brand);display:flex;align-items:center;justify-content:center}
/* contact */
.contact-photo{position:absolute;left:51px;top:3229px;width:503px;height:507px;background:linear-gradient(135deg,#2c3a4a,#6a4a2e 55%,#1a1f27)}
.form{position:absolute;left:586px;top:3228px;width:563px;height:508px;background:var(--panel);border:2px solid var(--line);border-radius:4px;padding:22px 22px}
.field{background:var(--white);height:58px;border-radius:4px;margin-bottom:17px;padding:0 20px;display:flex;align-items:center;font-size:15px}
.field.area{height:108px;align-items:flex-start;padding-top:16px}
.form .btn{border:none;padding:10px 32px;margin-top:0;font-size:13px}
/* footer */
.footer{position:absolute;top:3777px;left:0;width:1200px;height:301px;background:var(--footer);color:var(--white)}
.fcol{position:absolute;top:36px;font-size:15px}
.fcol h5{font-size:15px;font-weight:700;margin-bottom:12px}
.fcol li{list-style:none;height:34px}
.flogo{position:absolute;left:890px;top:32px;color:var(--brand)}
.flogo i{background:var(--brand)}
.fabout{position:absolute;left:890px;top:108px;width:260px;font-size:15px;line-height:22.5px}
.social{position:absolute;left:890px;top:190px;display:flex;gap:14px}
.social i{width:24px;height:24px;border-radius:50%;background:var(--white);display:block}
.copy{position:absolute;left:62px;right:62px;top:274px;border-top:1px solid #4a545a;padding-top:12px;text-align:center;font-size:12px;top:252px}
</style>
</head>
<body>

<div class="topbar">
  <span><svg width="12" height="12" viewBox="0 0 24 24" fill="none" stroke="#fff" stroke-width="2"><path d="M12 22s7-7 7-12a7 7 0 0 0-14 0c0 5 7 12 7 12z"/><circle cx="12" cy="10" r="2.5"/></svg>Sydney NSW, Australia</span>
  <span><svg width="13" height="12" viewBox="0 0 24 20" fill="none" stroke="#fff" stroke-width="2"><rect x="2" y="2" width="20" height="16" rx="2"/><path d="M2 4l10 7 10-7"/></svg>hello@brindlowelectrical.com.au</span>
  <span class="phone"><svg width="12" height="12" viewBox="0 0 24 24" fill="none" stroke="#fff" stroke-width="2"><path d="M5 3h4l2 5-3 2a12 12 0 0 0 6 6l2-3 5 2v4a2 2 0 0 1-2 2A18 18 0 0 1 3 5a2 2 0 0 1 2-2z"/></svg>02 7340 2291</span>
</div>

<header class="nav">
  <div class="logo"><i></i>Brindlow Electrical</div>
  <ul><li class="active">Home</li><li>About Us</li><li>Services</li><li>Latest Projects</li><li>Contact Us</li></ul>
  <span class="btn">Request a Quote</span>
</header>

<section class="hero" role="img" aria-label="Night view of illuminated commercial office buildings">
  <h1 class="display">Welcome to Brindlow<br>Electrical Solution</h1>
  <p>At Brindlow Electrical Solution, We Are Committed To Providing Safe, Efficient, And Reliable Electrical Solutions To Homes And Businesses Of All Sizes. Whether You Need A Quick Repair, An Installation, Or An Entire System Upgrade, Our Certified Team Is Here To Help You Every Step Of The Way.</p>
  <span class="btn">Book a Service</span>
  <div class="dots"><b></b><b></b><b></b><b></b></div>
</section>

<section class="about">
  <div class="photo" role="img" aria-label="Modern living room interior with pendant lights"></div>
  <div class="eyebrow">About Us</div>
  <h2 class="display">Your Trusted<br>Electrical<br>Solutions Partner</h2>
  <p>At Electrical, We Specialize In Delivering Expert Electrical Solutions For Both Residential And Commercial Needs.</p>
  <ul>
    <li><svg width="16" height="16" viewBox="0 0 16 16"><circle cx="8" cy="8" r="8" fill="#fff"/><path d="M4.5 8.2l2.3 2.2 4.7-4.8" stroke="#0b98e0" stroke-width="2" fill="none"/></svg>Experienced Professionals</li>
    <li><svg width="16" height="16" viewBox="0 0 16 16"><circle cx="8" cy="8" r="8" fill="#fff"/><path d="M4.5 8.2l2.3 2.2 4.7-4.8" stroke="#0b98e0" stroke-width="2" fill="none"/></svg>Customer-First Approach</li>
    <li><svg width="16" height="16" viewBox="0 0 16 16"><circle cx="8" cy="8" r="8" fill="#fff"/><path d="M4.5 8.2l2.3 2.2 4.7-4.8" stroke="#0b98e0" stroke-width="2" fill="none"/></svg>Affordable Pricing</li>
  </ul>
  <span class="btn">Learn More</span>
</section>

<section class="services">
  <div class="eyebrow">Our Services</div>
  <h2 class="sec-title display" style="top:1346px">Get Comprehensive Brindlow<br>Electrical Solution</h2>
  <article class="svc dark" style="left:54px">
    <div class="head"><h3>Residential Electrical Services</h3><p>Electrical Installations: Whether You're Building A New Home Or Renovating An Existing One,.</p></div>
    <div class="img" role="img" aria-label="Electrician working on a ladder inside a home" style="background:linear-gradient(135deg,#cfcac2,#8a7f74 60%,#5a5550)"></div>
  </article>
  <article class="svc" style="left:429px">
    <div class="head"><h3>Commercial Electrical Solutions</h3><p>Electrical Installations: Whether You're Building A New Home Or Renovating An Existing One,.</p></div>
    <div class="img" role="img" aria-label="Rooftop commercial ventilation units" style="background:linear-gradient(180deg,#eef0f2,#a9b0b6 60%,#6f777e)"></div>
  </article>
  <article class="svc" style="left:804px">
    <div class="head"><h3>Industrial Electrical Services</h3><p>Electrical Installations: Whether You're Building A New Home Or Renovating An Existing One,.</p></div>
    <div class="img" role="img" aria-label="Gloved hands wiring an industrial switchboard" style="background:linear-gradient(135deg,#7a6a55,#c9b58a 50%,#3d3a36)"></div>
  </article>
  <div class="center-btn" style="top:1846px"><span class="btn">View All Services</span></div>
</section>

<section class="testimonials">
  <div class="eyebrow" style="position:absolute;top:1948px;width:1200px;text-align:center">Testimonial</div>
  <h2 class="sec-title display" style="top:2003px">What Our Customers Are Saying</h2>
  <p style="position:absolute;top:2076px;left:220px;width:760px;text-align:center;font-size:15px;line-height:23px">Here's What Some Of Our Valued Clients Have To Say About Their Experience With Brindlow Electrical Solution</p>
  <article class="quote-card" style="left:68px">
    <div class="avatar" role="img" aria-label="Client portrait"></div>
    <h4>Clara Mendell</h4><div class="role">Homeowner</div>
    <div class="stars">★★★★</div>
    <blockquote>"I Was Amazed By The Professionalism And Efficiency Of The Brindlow Team. From Fixing A Plumbing Issue To Renovating My Kitchen, They Handled Everything With Utmost Care &amp; Attention To Detail."</blockquote>
  </article>
  <article class="quote-card" style="left:631px">
    <div class="avatar" role="img" aria-label="Client portrait" style="background:linear-gradient(135deg,#3a3a3a,#9a9a9a)"></div>
    <h4>Rowan Pike</h4><div class="role">Homeowner</div>
    <div class="stars">★★★★</div>
    <blockquote>"I Was Amazed By The Professionalism And Efficiency Of The Brindlow Team. From Fixing A Plumbing Issue To Renovating My Kitchen, They Handled Everything With Utmost Care &amp; Attention To Detail."</blockquote>
  </article>
  <div class="arrow" style="left:1031px"><svg width="22" height="16" viewBox="0 0 22 16" fill="none" stroke="#fff" stroke-width="2"><path d="M21 8H2M8 2L2 8l6 6"/></svg></div>
  <div class="arrow" style="left:1087px"><svg width="22" height="16" viewBox="0 0 22 16" fill="none" stroke="#fff" stroke-width="2"><path d="M1 8h19M14 2l6 6-6 6"/></svg></div>
</section>

<section class="projects">
  <h2 class="display">Latest Projects</h2>
  <article class="proj" style="left:63px;background:linear-gradient(180deg,#6f9fcc,#2f6aa5 60%,#0b4f95)" role="img" aria-label="Multi-storey office building under blue sky">
    <div class="tag">SYDNEY NSW,<br>AUSTRALIA</div>
    <div class="go"><svg width="22" height="16" viewBox="0 0 22 16" fill="none" stroke="#fff" stroke-width="2"><path d="M1 8h19M14 2l6 6-6 6"/></svg></div>
  </article>
  <article class="proj" style="left:432px;background:linear-gradient(180deg,#f2f3f4,#c6ccd1 55%,#7d8a78)" role="img" aria-label="Modern commercial building with parked cars"></article>
  <article class="proj" style="left:801px;background:linear-gradient(160deg,#1e5fb0,#4d8fd6 55%,#e6ebee)" role="img" aria-label="White apartment towers against blue sky"></article>
  <div class="center-btn" style="top:3056px"><span class="btn">View All Projects</span></div>
</section>

<section class="contact">
  <h2 class="sec-title display" style="top:3155px">Contact Us</h2>
  <div class="contact-photo" role="img" aria-label="Electrician in hard hat and safety glasses working on a panel with a screwdriver"></div>
  <form class="form">
    <div class="field">Name :</div>
    <div class="field">Last Name :</div>
    <div class="field">Email :</div>
    <div class="field">Phone Number :</div>
    <div class="field area">How can I Help You ?</div>
    <span class="btn">Submit</span>
  </form>
</section>

<footer class="footer">
  <div class="fcol" style="left:62px"><h5>Information</h5><ul><li>Home</li><li>About Us</li><li>Services</li><li>Our Products</li><li>Contact Us</li></ul></div>
  <div class="fcol" style="left:333px"><h5>Resources</h5><ul><li>Terms Of Condition</li><li>Privacy Policy</li><li>Cookies</li></ul></div>
  <div class="fcol" style="left:608px"><h5>Quick Contact</h5><ul><li>Sydney NSW, Australia</li><li>hello@brindlowelectrical.com.au</li><li>02 7340 2291</li></ul></div>
  <div class="logo flogo"><i></i>Brindlow Electrical</div>
  <p class="fabout">Whether You're Looking For Residential, Commercial, Or Industrial Electrical Solutions,</p>
  <div class="social" aria-label="Social media links"><i></i><i></i><i></i></div>
  <div class="copy">2024 Copyright ©Brindlow Electrical Solution Inc All Rights Reserved</div>
</footer>

</body>
</html>
```